Business Card Design

My company is a health food catering and delivery business. Our colours are a bright turquiose green/blue, black, white and natural brown based beige. I would like the front of my card (working from the outside in; with a turquoise green boarder -quite thick, with a thin black line separating the turquoise boarder from the beige inside the remaining space of the front of the card with my logo in the centre. This should be all that appears on the front.

On the back I would like all the information displayed above on the beige coloured card, with the blurb in the bright turquoise and my contact information in black please. I would like my business name central - Harvest Crown Kitchen and immediately below with a right alignment - ...Dine like a Monarch
Below this should follow all that I have displayed above with a left alignment.

Target Market(s)

Cafes, restaurants, individuals, buying agents & super markets

Industry/Entity Type

Catering

Contact Information for Business Card

BACK OF BUSINESS CARD:
Harvest Crown Kitchen
...Dine like a Monarch
Deliciously healthy foods - free from gluten, lactose, cane sugar, trans-fat, GMO corn, soy & rice, no artificial flavours, colours or preservatives.
Prepared fresh from locally sourced ingredients, delivered to your door! For individuals, families, corporate, cafes, restaurants & event catering for Toowoomba & surrounds!

PH: 0491 538 207 // orders@harvestcrownkitchen.example
www.harvestcrownkitchen.example
www.socialpage.example/harvestcrownkitchen

Requirements
Must have
• Please supply a modern, easy to read text that will blend nicely with my logo text.
Nice to have
• I really want my business cards to stand out as these will be the template for brochures, menus and website designers to draw inspiration from!
Should not have
• Please do not use Arial, Tahoma or Times Roman text.

```html
<!DOCTYPE html>
<html lang="en">
<head>
<meta charset="utf-8">
<title>Harvest Crown Kitchen – Business Card</title>
<link rel="stylesheet" href="https://fonts.googleapis.com/css2?family=Barlow+Condensed:ital,wght@0,400;0,700;1,400&display=swap">
<style>
  :root {
    --teal: #45ba9e;
    --beige: #ba9678;
    --beige-deep: #a9876a;
    --ink: #0d0d0d;
    --paper: #ffffff;
  }
  * { box-sizing: border-box; margin: 0; padding: 0; }
  html, body { width: 888px; height: 1200px; overflow: hidden; background: var(--paper); }
  body { position: relative; font-family: "Barlow Condensed", "Arial Narrow", sans-serif; color: var(--ink); }

  .card-face { position: absolute; left: 0; width: 888px; background: var(--teal); }
  .card-front { top: 30px; height: 548px; }
  .card-back { top: 626px; height: 548px; }

  .card-inner {
    position: absolute; left: 29px; top: 28px; width: 830px; height: 492px;
    background: var(--beige); border: 1.5px solid var(--ink);
  }

  /* Front: logo area */
  .logo-art {
    position: absolute; left: 232px; top: 110px; width: 366px; height: 230px;
    border-radius: 12px;
    background: linear-gradient(180deg, #f4f1ec 0%, #d9d2c8 100%);
  }
  .logo-name {
    position: absolute; left: 0; right: 0; top: 348px; text-align: center;
    font-weight: 700; font-size: 38px; color: var(--ink);
  }

  /* Back: information */
  .brand-block { position: absolute; left: 0; right: 0; top: 22px; text-align: center; }
  .brand-name { font-weight: 700; font-size: 64px; line-height: 1; letter-spacing: -0.5px; }
  .brand-tagline {
    position: absolute; right: 180px; top: 66px;
    font-style: italic; font-size: 22px; line-height: 1;
  }
  .blurb {
    position: absolute; left: 30px; right: 30px; top: 170px;
    text-align: center; font-size: 26px; line-height: 36px; letter-spacing: -0.3px;
  }
  .contact-rule { position: absolute; left: 0; right: 0; top: 418px; border-top: 1px solid var(--beige-deep); }
  .contact-line {
    position: absolute; left: 0; right: 0; top: 432px; text-align: center;
    font-size: 21px; line-height: 30px; white-space: nowrap;
  }
  .contact-line b { font-weight: 700; }
  .contact-line .sep { margin: 0 4px; }
  .social-mark {
    display: inline-block; width: 12px; height: 12px; background: var(--ink);
    margin-right: 3px; vertical-align: 0;
  }
</style>
</head>
<body>
  <section class="card-face card-front">
    <div class="card-inner">
      <div class="logo-art" role="img" aria-label="Line illustration of a chef in hat and apron holding a whisk and a frying pan"></div>
      <div class="logo-name">Harvest Crown Kitchen</div>
    </div>
  </section>

  <section class="card-face card-back">
    <div class="card-inner">
      <header class="brand-block">
        <h1 class="brand-name">Harvest Crown Kitchen</h1>
        <p class="brand-tagline">...Dine like a Monarch</p>
      </header>
      <p class="blurb">Deliciously healthy foods - free from gluten, lactose, cane sugar, trans-fat, GMO corn,<br>soy &amp; rice, no artificial flavours, colours or preservatives. Prepared fresh from locally<br>sourced ingredients, delivered to your door! For individuals, families, corporate,<br>cafes, restaurants &amp; event catering for Toowoomba &amp; surrounds!</p>
      <div class="contact-rule"></div>
      <p class="contact-line"><b>P:</b> 0491 538 207<span class="sep">|</span><b>E:</b> orders@<span class="sep">|</span><b>W:</b> harvestcrownkitchen.example<span class="sep">|</span><span class="social-mark"></span>/harvestcrownkitchen</p>
    </div>
  </section>
</body>
</html>
```